Business Card Design

Cedar Gate Rentals
Cedar Gate Rentals is a high end home rental leasing company that provides exquisite properties in niche markets. We are a small family owned business that considers our clients not as renters, but as friends. Every property we buy must be brought up to our high standards before it is offered on the market. The properties that we lease are exceptional, "move in" ready homes. This allows for the client to take pride in their lease as if it was their own home. To put it another way; we do not lease a property that we would not live in ourselves.

Target Market(s)

Couples making $100K or more

Industry/Entity Type

Business

Requirements
Must have
• Some sort of logo
Nice to have
• good slogan
Should not have
• Pink

```html
<!DOCTYPE html>
<html lang="en">
<head>
<meta charset="utf-8">
<title>Cedar Gate Rentals — Business Card</title>
<link rel="stylesheet" href="https://fonts.googleapis.com/css2?family=Oxygen:wght@400;700&display=swap">
<style>
  :root {
    --card-bg: #e9e9ef;
    --row-light: #f2f2f3;
    --brand-blue: #3373fb;
    --brand-teal: #2286b5;
    --brand-mint: #5cfb9a;
    --white: #ffffff;
  }
  html, body {
    margin: 0;
    padding: 0;
    width: 1200px;
    height: 720px;
    overflow: hidden;
    background: var(--card-bg);
  }
  .card {
    position: relative;
    width: 1200px;
    height: 720px;
    background: var(--card-bg);
    font-family: "Oxygen", sans-serif;
    overflow: hidden;
  }
  .brand {
    position: absolute;
    left: 104px;
    top: 258px;
    display: flex;
    align-items: center;
    gap: 18px;
  }
  .brand-square {
    width: 30px;
    height: 30px;
    background: var(--brand-blue);
  }
  .brand-name {
    margin: 0;
    font-size: 40px;
    font-weight: 700;
    letter-spacing: 2.5px;
    text-transform: uppercase;
    color: var(--brand-teal);
    line-height: 1;
  }
  .title-band {
    position: absolute;
    left: 0;
    top: 341px;
    width: 1200px;
    height: 82px;
    background: var(--brand-blue);
    display: flex;
    align-items: center;
    padding-left: 102px;
    box-sizing: border-box;
    color: var(--white);
  }
  .person-name {
    font-size: 44px;
    font-weight: 700;
    letter-spacing: 4px;
    text-transform: uppercase;
  }
  .person-role {
    font-size: 30px;
    letter-spacing: 3px;
    margin-left: 6px;
    position: relative;
    top: -4px;
  }
  .contact-list {
    position: absolute;
    left: 0;
    top: 423px;
    width: 1200px;
    margin: 0;
    padding: 0;
    list-style: none;
  }
  .contact-item {
    height: 52px;
    display: flex;
    align-items: center;
    padding-left: 102px;
    color: var(--brand-blue);
    font-size: 23px;
  }
  .contact-item:nth-child(even) { background: var(--row-light); }
  .contact-phone { letter-spacing: 3px; }
  .contact-email { letter-spacing: 6px; }
  .contact-web { letter-spacing: 2px; }
</style>
</head>
<body>
  <div class="card">
    <div class="brand">
      <span class="brand-square" aria-hidden="true"></span>
      <h1 class="brand-name">Cedar Gate Rentals</h1>
    </div>

    <div class="title-band">
      <span class="person-name">Daniel Harlow</span>
      <span class="person-role">director</span>
    </div>

    <ul class="contact-list">
      <li class="contact-item contact-address">41 Linden Street, Hartford</li>
      <li class="contact-item contact-phone">04 38 21 56 17</li>
      <li class="contact-item contact-email">dharlow@mail.com</li>
      <li class="contact-item contact-web">www.CedarGateRentals.com</li>
    </ul>
  </div>
</body>
</html>
```